zorvantix Web Design Project

It is a virtual assistance/concierge company that helps the busy professional by remotely providing administrative, technical and/or creative business support services, specializing in the medical device industry. Company name is zorvantix.
(website will be zorvantix.com)

Allowing things to be done without taking time away from more urgent issues or family/personal time. Partnering with a VA reduces stress, protects cash flow, eliminates administrative hassles, and enables business people to find the success they originally set out to achieve. Saves small businesses and/or individuals on overhead, salary, et. Work is done remotely to offer administrative, clerical, typing and specialist service assistance on a regular, ad-hoc or emergency cover basis.

Though we are capable of addressing the needs of medical professionals and industry representatives due to our experience and knowledge (sales, HCC guidelines, etc.) we do not want to be limited to that market only.

Target Market(s)

Target market would be M/F, 30-50, National, busy, Alpha, entrepreneurs and industry professionals who want/need to do more without sacrifice of life

Industry/Entity Type

Industry

Requirements
Nice to have
• We do have a logo designed via the MarqueLoom website that can/should be included. Logo is uploaded.

```html
<!DOCTYPE html>
<html lang="en">
<head>
<meta charset="utf-8">
<title>zorvantix — Virtual Assistance</title>
<link rel="stylesheet" href="https://fonts.googleapis.com/css2?family=Noto+Sans&family=Tinos:ital@1&display=swap">
<style>
  :root {
    --page-bg: #ffffff;
    --nav-band: rgba(230, 230, 230, 0.88);
    --navy: #1c3150;
    --accent-red: #c8302c;
    --wine: #8e3535;
    --wine-dark: #7a2b2b;
    --rule: #d9a3a3;
    --thumb-border: #b86a6a;
    --arrow: #7d8a99;
    --ink-light: #f6eaea;
  }
  * { box-sizing: border-box; margin: 0; padding: 0; }
  html, body { width: 1200px; height: 833px; overflow: hidden; background: var(--page-bg); }
  .page { position: relative; width: 1200px; height: 833px; overflow: hidden; }

  .hero-photo {
    position: absolute; left: 130px; top: 0; width: 960px; height: 610px;
    background: radial-gradient(ellipse at 70% 45%, #e9c9b8 0%, #cfa896 30%, #8a6a5c 60%, #e8e2de 100%);
  }

  .call-line {
    position: absolute; top: 17px; right: 217px;
    font-family: "Tinos", serif; font-style: italic; font-size: 18px; color: #1a1a1a;
  }

  .nav-band {
    position: absolute; left: 0; top: 47px; width: 1200px; height: 68px;
    background: var(--nav-band);
  }
  .brand {
    position: absolute; left: 205px; top: 11px;
    display: flex; align-items: center; gap: 8px;
    font-family: "Noto Sans", sans-serif; font-size: 32px; color: var(--navy);
  }
  .brand-dot { width: 14px; height: 14px; border-radius: 50%; background: var(--navy); }
  .main-nav {
    position: absolute; left: 586px; top: 25px; display: flex;
    font-family: "Noto Sans", sans-serif; font-size: 15px;
  }
  .main-nav a {
    color: var(--navy); text-decoration: none; padding: 0 14px;
    border-left: 1px solid #b9b9b9; line-height: 24px;
  }
  .main-nav a:first-child { border-left: none; color: var(--accent-red); }

  .thumb-strip {
    position: absolute; left: 0; top: 550px; width: 1200px; height: 60px;
    border-top: 1px solid var(--rule); background: rgba(255, 255, 255, 0.75);
  }
  .thumb-arrow { position: absolute; top: 21px; }
  .thumb-arrow.prev { left: 204px; }
  .thumb-arrow.next { left: 984px; }
  .thumbs { position: absolute; left: 236px; top: 9px; display: flex; gap: 8px; }
  .thumb {
    width: 59px; height: 46px; border: 2px solid var(--thumb-border);
    background: linear-gradient(160deg, #cfd8dc, #6f8c7c 60%, #3f5c4a);
  }
  .thumb.team { background: linear-gradient(160deg, #f3ece8, #b08a78 60%, #3a3a3a); }
  .thumb.room { background: linear-gradient(160deg, #dfe5ee, #8fa2bd 60%, #4b5e7a); }

  .welcome {
    position: absolute; left: 0; top: 610px; width: 1200px; height: 223px;
    background: radial-gradient(ellipse at 50% 40%, var(--wine) 55%, var(--wine-dark) 100%);
    color: var(--ink-light); font-family: "Tinos", serif; font-style: italic;
  }
  .welcome h1 {
    position: absolute; top: 18px; width: 100%; text-align: center;
    font-weight: 400; font-size: 27px; color: #ffffff;
  }
  .welcome p.intro {
    position: absolute; left: 200px; top: 57px; width: 800px;
    font-size: 15px; line-height: 24px;
  }
  .site-footer {
    position: absolute; top: 186px; width: 100%; text-align: center;
    font-size: 9px; line-height: 14px; letter-spacing: 0.3px;
  }
  .site-footer b { color: #ffffff; text-decoration: underline; }
</style>
</head>
<body>
<div class="page">
  <div class="hero-photo" role="img" aria-label="Photo of three smiling call-centre staff wearing headsets"></div>

  <div class="call-line">Call us : 1800 - 55 - 302718</div>

  <header class="nav-band">
    <div class="brand"><span class="brand-dot"></span>zorvantix</div>
    <nav class="main-nav">
      <a href="#">Home</a>
      <a href="#">About Us</a>
      <a href="#">Our Services</a>
      <a href="#">Contact Us</a>
    </nav>
  </header>

  <div class="thumb-strip">
    <svg class="thumb-arrow prev" width="12" height="22" viewBox="0 0 12 22"><polyline points="10,2 2,11 10,20" fill="none" stroke="var(--arrow)" stroke-width="3"/></svg>
    <div class="thumbs">
      <div class="thumb team" role="img" aria-label="Thumbnail of headset team"></div>
      <div class="thumb room" role="img" aria-label="Thumbnail of medical equipment room"></div>
      <div class="thumb" role="img" aria-label="Thumbnail of operating theatre"></div>
      <div class="thumb room" role="img" aria-label="Thumbnail of medical device"></div>
      <div class="thumb room" role="img" aria-label="Thumbnail of medical equipment room"></div>
      <div class="thumb" role="img" aria-label="Thumbnail of operating theatre"></div>
      <div class="thumb room" role="img" aria-label="Thumbnail of medical device"></div>
      <div class="thumb room" role="img" aria-label="Thumbnail of medical equipment room"></div>
      <div class="thumb" role="img" aria-label="Thumbnail of operating theatre"></div>
      <div class="thumb room" role="img" aria-label="Thumbnail of medical equipment room"></div>
      <div class="thumb" role="img" aria-label="Thumbnail of operating theatre"></div>
    </div>
    <svg class="thumb-arrow next" width="12" height="22" viewBox="0 0 12 22"><polyline points="2,2 10,11 2,20" fill="none" stroke="var(--arrow)" stroke-width="3"/></svg>
  </div>

  <section class="welcome">
    <h1>Welcome to our site</h1>
    <p class="intro">It is a virtual assistance/concierge company that helps the busy professional by remotely providing administrative, technical and/or creative business support services, specializing in the medical device industry. Company name is zorvantix. It is a virtual assistance/concierge company that helps the busy professional by remotely providing administrative, technical and/or creative business support services, specializing in the medical device industry. Company name is zorvantix.</p>
    <footer class="site-footer">© 2012, All rights reserved. <b>zorvantix</b><br>Terms &amp; Privacy Policy</footer>
  </section>
</div>
</body>
</html>
```